Prepared ready to cook meal delivery service needs a flyer design

We need a flyer design for a startup company based in Cape Town, South Africa. I've attached a few flyer designs that I like.

The company is called 'Pemblo' and our website will be found at pemblo.co.za. We don't have a logo yet.

Flyer text:

Pemblo
Simply sizzle

Do you feel like a home cooked meal but don't like shopping, peeling, chopping, cooking, or cleaning up?

We deliver ready to roast free range chicken and fresh vegetables to your door.

To order: SMS your name to 074 318 6149 and we'll call you back.

Only the best ingredients used
Free range chickens. Fresh herbs and vegetables. Virgin olive oil.

No bad carbs!

Ready to roast Free range chicken and fresh veggies
For 2 R99
For 4 R139
Updates

Wording of flyer updated.

Target Market(s)

Local Cape Townians that hate grocery shopping and need help saving time preparing meals.

Industry/Entity Type

Delivery Service

Requirements
Must have
• To find out more: SMS your name to 074 318 6149

```html
<!DOCTYPE html>
<html lang="en">
<head>
<meta charset="utf-8">
<title>Pemblo – Simply sizzle</title>
<link rel="stylesheet" href="https://fonts.googleapis.com/css2?family=Oswald:wght@400;500&family=Raleway:wght@300;400&family=Open+Sans:wght@400;600;700&display=swap">
<style>
  :root {
    --page-bg: #e8e4df;
    --brown-dark: #40352c;
    --brown-mid: #5e5043;
    --cream: #f3e6c4;
    --cream-soft: #efe7d6;
    --orange: #f39a1e;
    --orange-deep: #e0701c;
    --orange-fold: #b5581a;
    --number-red: #8e2a1c;
    --ink: #2b2521;
    --dish-white: #f7f5f1;
  }
  * { margin: 0; padding: 0; box-sizing: border-box; }
  html, body {
    width: 1200px; height: 848px; overflow: hidden;
    background: var(--page-bg);
  }
  .canvas { position: relative; width: 1200px; height: 848px; }

  .flyer {
    position: absolute; left: 320px; top: 26px;
    width: 494px; height: 698px;
    transform: scale(1.139); transform-origin: top left;
    background:
      radial-gradient(ellipse 190px 160px at 50% 14%, rgba(255,245,225,.5), rgba(255,245,225,0) 100%),
      linear-gradient(180deg, var(--brown-mid) 0%, var(--brown-dark) 55%, #4b4035 100%);
    box-shadow: 0 4px 14px rgba(0,0,0,.25);
  }

  .brand {
    position: absolute; left: 0; right: 0; top: 58px;
    display: flex; flex-direction: column; align-items: center;
  }
  .brand-row { display: flex; align-items: center; gap: 10px; }
  .brand-dot { width: 14px; height: 14px; border-radius: 50%; background: var(--orange); }
  .brand-name {
    font-family: "Oswald", sans-serif; font-weight: 500;
    font-size: 42px; line-height: 52px; letter-spacing: 1px; color: var(--cream);
  }
  .brand-tagline {
    margin-top: 4px;
    font-family: "Raleway", sans-serif; font-weight: 400;
    font-size: 13px; letter-spacing: 3px; text-transform: uppercase; color: var(--cream-soft);
  }

  .dotted-rule {
    position: absolute; left: 22px; right: 22px; height: 4px;
    background-image: radial-gradient(circle, var(--cream-soft) 1.3px, transparent 1.6px);
    background-size: 7.4px 4px; background-repeat: repeat-x;
  }
  .dotted-rule.top { top: 200px; }
  .dotted-rule.bottom { top: 288px; }

  .headline {
    position: absolute; left: 0; right: 0; top: 207px; text-align: center;
    font-family: "Oswald", sans-serif; font-weight: 500;
    font-size: 30px; line-height: 40px; color: var(--cream);
  }
  .subline {
    position: absolute; left: 0; right: 0; top: 248px; text-align: center;
    font-family: "Raleway", sans-serif; font-weight: 300;
    font-size: 12px; line-height: 15px; color: var(--cream-soft);
  }

  .food-photo {
    position: absolute; left: 7px; top: 339px; width: 480px; height: 295px;
    background: var(--dish-white); border-radius: 4px 4px 0 0; overflow: hidden;
  }
  .food-photo-fill {
    position: absolute; inset: 14px 12px 0 12px;
    background:
      radial-gradient(ellipse 150px 110px at 48% 48%, #e9b76a 0%, #d49448 55%, rgba(212,148,72,0) 100%),
      linear-gradient(135deg, #8b3a3a 0%, #a7743b 35%, #c98c44 55%, #7c8a3c 80%, #b33a2a 100%);
  }

  .promise-tag {
    position: absolute; left: -6px; top: 320px; width: 185px; height: 84px;
    background: var(--orange); border-radius: 0 8px 8px 0;
    padding: 4px 0 0 16px;
    font-family: "Oswald", sans-serif; font-weight: 400; font-size: 10px;
    color: #fff; line-height: 15px;
  }
  .promise-tag::before {
    content: ""; position: absolute; left: 0; top: 84px;
    border-top: 6px solid var(--orange-fold); border-left: 6px solid transparent;
  }
  .promise-list {
    list-style: none; display: grid;
    grid-template-columns: 80px 80px; grid-auto-flow: column;
    grid-template-rows: repeat(4, 15px);
  }
  .promise-list li::before { content: "●"; font-size: 8px; margin-right: 2px; vertical-align: 1px; }
  .promise-note {
    font-family: "Raleway", sans-serif; font-size: 8.5px; line-height: 12px;
    color: #fff7e8; margin-left: -4px;
  }

  .benefits {
    position: absolute; left: 0; top: 566px; width: 484px; height: 62px;
    background: rgba(255,255,255,.72); padding: 4px 0 0 6px;
    font-family: "Open Sans", sans-serif; font-size: 8.4px; line-height: 11px;
    color: var(--ink);
  }
  .benefits h3 { font-size: 8.6px; font-weight: 700; }
  .price { font-weight: 700; }

  .cta-bar {
    position: absolute; left: 0; top: 634px; width: 494px; height: 46px;
    background: var(--orange);
    display: flex; align-items: center; justify-content: center;
    font-family: "Oswald", sans-serif; font-weight: 500;
    font-size: 19px; color: var(--cream); white-space: nowrap;
  }
  .cta-number { color: var(--number-red); font-size: 24px; margin: 0 6px; }

  .web-bar {
    position: absolute; left: 0; top: 680px; width: 494px; height: 18px;
    background: var(--orange-deep);
    display: flex; align-items: center; justify-content: center;
    font-family: "Open Sans", sans-serif; font-weight: 700;
    font-size: 8px; letter-spacing: 2.6px; color: #fde7cf;
  }
</style>
</head>
<body>
<div class="canvas">
  <article class="flyer">
    <header class="brand">
      <div class="brand-row">
        <span class="brand-dot"></span>
        <span class="brand-name">Pemblo</span>
      </div>
      <p class="brand-tagline">Simply sizzle</p>
    </header>

    <div class="dotted-rule top"></div>
    <h1 class="headline">THE EASY WAY TO COOK LIKE A CHEF</h1>
    <p class="subline">We deliver ready to roast free range chicken<br>and fresh vegetables to your door.</p>
    <div class="dotted-rule bottom"></div>

    <div class="food-photo">
      <div class="food-photo-fill" role="img" aria-label="Roast chicken with roasted vegetables and herbs in a white baking dish"></div>
    </div>

    <aside class="promise-tag">
      <ul class="promise-list">
        <li>NO SHOPPING</li>
        <li>NO PEELING</li>
        <li>NO CHOPPING</li>
        <li>NO CLEANING UP</li>
        <li>NO BAD CARBS</li>
      </ul>
      <p class="promise-note">Only the best ingredients used.</p>
    </aside>

    <section class="benefits">
      <h3>Only the best ingredients used:</h3>
      <p>Free range chickens. Fresh herbs and vegetables. Virgin olive oil. No bad carbs!</p>
      <p>Ready to roast free range chicken and fresh veggies: <span class="price">For 2 R99</span> · <span class="price">For 4 R139</span></p>
      <p>To order: SMS your name to 074 318 6149 and we'll call you back.</p>
    </section>

    <div class="cta-bar">SMS YOUR NAME TO<span class="cta-number">074 318 6149</span>TO FIND OUT MORE</div>
    <div class="web-bar">www.pemblo.co.za</div>
  </article>
</div>
</body>
</html>
```